Mailchimp Email Design for Weekly New Products Email

We would like to send a weekly email to our customers highlighting four of the new jewelry pieces we have for sale each week. The email should be professionally looking, and have the same look and feel of our website, calvinmarlowgems.com. The template would have our logo on the top or left header, and would then have a block of text which would stay the same each week. This block would say "This weeks new arrivals won't last long, shop now with discount code "EMAIL10" to receive 10% off your entire purchase!"
Then below that, there would space for four images, which I will need to change every week. Below each image, there should be room for a title description of the image, which I will need to change each week. An example title would be "18k Yellow Gold Curb Necklace"
Then below the found images, maybe a black action button that says "SHOP NOW". Also, each of the images should be clickable links, which I can edit to add the link to the specific item.
I have attached a few images so you can use them for the mockup. Also, if there are any other ideas you have to make it look better please do!
Thanks,
Ned
It only allowed me to upload one image, so I uploaded the EPS file of our logo. You can use the product images from our website, calvinmarlowgems.com for the product images for now.

```html
<!DOCTYPE html>
<html lang="en">
<head>
<meta charset="utf-8">
<title>Calvin Marlow Gems – New Arrivals</title>
<link rel="stylesheet" href="https://fonts.googleapis.com/css2?family=Cinzel:wght@400&family=Great+Vibes&family=Poppins:wght@400;700&family=Montserrat:wght@500;600&family=Libre+Baskerville&display=swap">
<style>
  :root {
    --navy: #272d3b;
    --navy-text: #2c3344;
    --page: #f3f3f3;
    --white: #ffffff;
    --card-border: #d6d6d6;
    --rule: #d9d9d9;
    --ink: #222222;
    --photo-light: #f1f0ee;
    --photo-mid: #dcd9d3;
  }
  * { box-sizing: border-box; margin: 0; padding: 0; }
  html, body { width: 1200px; height: 2590px; overflow: hidden; background: var(--white); }
  body { font-family: "Poppins", sans-serif; color: var(--ink); }

  .preheader {
    height: 69px; display: flex; align-items: center; justify-content: center;
    border-bottom: 2px solid var(--rule);
    font-family: "Montserrat", sans-serif; font-size: 20px; font-weight: 500; color: #333;
  }

  .brand { text-align: center; }
  .brand-name { font-family: "Cinzel", serif; font-weight: 400; letter-spacing: 1px; line-height: 1; }
  .brand-tagline { font-family: "Cinzel", serif; font-weight: 400; margin-top: 14px; letter-spacing: 2px; }

  .masthead { height: 214px; display: flex; align-items: center; justify-content: center; color: var(--navy); }
  .masthead .brand-name { font-size: 62px; }
  .masthead .brand-tagline { font-size: 24px; }

  .promo {
    height: 403px; background: var(--navy); color: var(--white);
    text-align: center; padding-top: 38px;
  }
  .promo-headline { font-family: "Great Vibes", cursive; font-size: 62px; line-height: 64px; font-weight: 400; }
  .promo-copy { font-size: 31px; margin-top: 28px; line-height: 1.2; }
  .promo-code { font-size: 60px; font-weight: 700; line-height: 1.1; margin: 8px 0 10px; }

  .arrivals { height: 1524px; background: var(--page); padding-top: 38px; }
  .arrivals-title {
    text-align: center; font-family: "Montserrat", sans-serif; font-weight: 600;
    font-size: 45px; letter-spacing: 3px; color: var(--navy-text);
  }
  .product-grid {
    width: 901px; margin: 30px auto 0;
    display: grid; grid-template-columns: 435px 435px; column-gap: 31px; row-gap: 31px;
  }
  .product-card {
    display: block; height: 602px; background: var(--white);
    border: 2px solid var(--card-border); text-decoration: none; color: var(--ink);
    padding: 26px 26px 0; text-align: center;
  }
  .product-photo { height: 302px; background: linear-gradient(180deg, var(--photo-light), var(--photo-mid)); }
  .product-photo.on-white { background: radial-gradient(ellipse at center, #e6d3a0 0%, #f7f3ea 35%, #ffffff 60%); }
  .product-name { font-size: 22px; line-height: 34px; margin: 36px auto 0; width: 330px; height: 102px; }
  .product-price { font-family: "Libre Baskerville", serif; font-size: 40px; margin-top: 40px; color: #2a2a2a; }

  .shop-button {
    display: flex; align-items: center; justify-content: center;
    width: 408px; height: 90px; margin: 36px auto 0; background: var(--navy);
    color: var(--white); font-family: "Montserrat", sans-serif; font-weight: 600;
    font-size: 31px; letter-spacing: 3px; text-decoration: none;
  }

  .site-footer { height: 273px; background: var(--navy); color: var(--white); text-align: center; padding-top: 36px; }
  .site-footer .brand-name { font-size: 54px; }
  .site-footer .brand-tagline { font-size: 22px; margin-top: 10px; }
  .contact { font-family: "Montserrat", sans-serif; font-size: 23px; margin-top: 30px; letter-spacing: 0.5px; }
  .contact b { font-weight: 600; }
  .contact .divider { margin: 0 18px; }
  .address { font-family: "Montserrat", sans-serif; font-size: 23px; margin-top: 14px; letter-spacing: 0.5px; }

  .social { height: 107px; display: flex; justify-content: center; align-items: center; gap: 26px; }
  .social-dot { width: 76px; height: 76px; border-radius: 50%; background: var(--navy); display: block; }
</style>
</head>
<body>
  <div class="preheader">DON'T SEE THIS EMAIL PROPERLY? VIEW IN WEB BROWSER</div>

  <header class="masthead">
    <div class="brand">
      <div class="brand-name">Calvin Marlow Gems</div>
      <div class="brand-tagline">Fine Vintage &amp; Estate Jewelry</div>
    </div>
  </header>

  <section class="promo">
    <h1 class="promo-headline">This Weeks<br>New Arrivals Won't Last Long</h1>
    <p class="promo-copy">shop now with discount code</p>
    <p class="promo-code">"EMAIL10"</p>
    <p class="promo-copy" style="margin-top:0">to receive 10% off your entire purchase!"</p>
  </section>

  <main class="arrivals">
    <h2 class="arrivals-title">NEW ARRIVALS</h2>
    <div class="product-grid">
      <a class="product-card" href="#">
        <div class="product-photo on-white" role="img" aria-label="Two tone gold wire flex cuff bangle bracelet"></div>
        <p class="product-name">Renata Colli 18k Yellow White Gold Two Tone Wire Flex Cuff Bangle Bracelet</p>
        <p class="product-price">$1699.00</p>
      </a>
      <a class="product-card" href="#">
        <div class="product-photo" role="img" aria-label="Gold and pearl X link bracelet on a white display stand"></div>
        <p class="product-name">Halloway Brothers 18k Gold and Pearls Vintage X Link Bracelet 7"</p>
        <p class="product-price">$2,799.00</p>
      </a>
      <a class="product-card" href="#">
        <div class="product-photo" role="img" aria-label="Yellow gold foxtail chain bracelet on a white display stand"></div>
        <p class="product-name">18k Yellow Gold Vintage 4.5mm Riccio Foxtail Link Chain Bracelet 7.5"</p>
        <p class="product-price">$799.00</p>
      </a>
      <a class="product-card" href="#">
        <div class="product-photo" role="img" aria-label="Wide Italian yellow gold bracelet on a white display stand"></div>
        <p class="product-name">18k Italian Yellow Gold Vintage Fancy 25mm Wide Ladies Bracelet 8"</p>
        <p class="product-price">$2,199.00</p>
      </a>
    </div>
    <a class="shop-button" href="#">SHOP NOW</a>
  </main>

  <footer class="site-footer">
    <div class="brand">
      <div class="brand-name">Calvin Marlow Gems</div>
      <div class="brand-tagline">Fine Vintage &amp; Estate Jewelry</div>
    </div>
    <p class="contact"><b>Phone:</b> 8888 .5550.2417<span class="divider">|</span><b>Email:</b> info@calvinmarlowgems.com</p>
    <p class="address">Lindenhoflaan 24, 3811 KP Amersfoort, The Netherlands</p>
  </footer>

  <nav class="social" aria-label="Social links">
    <a class="social-dot" href="#" aria-label="Social profile one"></a>
    <a class="social-dot" href="#" aria-label="Social profile two"></a>
  </nav>
</body>
</html>
```